パック詰めしたカニ身を入れる袋のデザインを依頼させていただきます。中の商品が見えるように、また通販のお客様だけでなく、デパートの食品売り場や高級スーパーで手にとっていただけるような、高級感のあるデザイン案をお願いします。イメージは『和モダン』です。
▼デザインの仕様▼
【袋サイズ】W200×H300(mm)
【デザインしていただく部分】W200×H270(mm)
※袋下30mmは空けておいてください。
商品が入った状態の参考画像は添付ファイル①を参照
(今回は袋のデザインをお願いします)
【色の数】4色まで
【材質】PP

▼記載内容▼※文字サイズ、字体、配置はおまかせいたします。
【商品名】右記よりどれか(かに身 ・ カニ身 ・ 蟹身)
【会社名】北岡商店
【賞味期限印刷用スペース】W30×H10(mm)※白抜きで
【商品特長】以下よりいくつか選択の上記載してください。
※表現は自由に変更してください。
・茹でへのこだわり(アルカリ水、瀬波の白粒使用)
・兵庫 香住港産
・日本海の深層水で育まれた
・みずみずしい
・カニ本来の甘み
【イメージ画像】添付ファイル②参照
※こちらは使っていただいてもいただかなくてもどちらでも結構です。
赤系、グレー系、黒・ゴールド等、高級感のある色
• 高解像度JPG (.jpg)
• イラストレーター形式 (.ai)
参考画像追記しておきます
多くのご提案ありがとうございます。
ご検討いただいているランサーの皆様に弊社よりお願いがあります。

1.依頼開始当初より記載しておりました、『和モダン』というイメージにあまり固執されすぎることなく、各ランサー様の自由な発想でデザインしていただきたい。
2.添付ファイル②のカニの画像は使用しないでください。

大変申し訳ございませんが、既にご提案いただいております皆様も、上記の点を踏まえまして、再度のご検討、ご提案いただければと思います。
残り日数少ない中、急な変更ではございますが何卒宜しくお願い致します。
上記変更に伴い、締め切りを1日延長させていただきます。
よろしくお願いいたします

ご質問等ございましたら、お気軽にお問い合わせ下さい。

・伝えたいことを見ただけで分かりやすくとらえることができる。
・主張しすぎないデザインの中に、高級感、上品さが感じ取れる。
・バランスがよく、中のカニ身を引き立ててくれると感じた。

皆様の貴重なお時間を、弊社依頼に費やしていただきまして、誠にありがとうございました。
今回見送らせていただいた皆様のご提案の中にも、素晴らしいデザインのものが数多くありました。今後もTesmora内におきまして他製品のパッケージやパンフレット等の依頼ができればと思っております。その際は是非また、素敵なご提案をお願いいたします。

```html
<!DOCTYPE html>
<html lang="ja">
<head>
<meta charset="utf-8">
<title>特選 かに身 パッケージ</title>
<link rel="stylesheet" href="https://fonts.googleapis.com/css2?family=Shippori+Mincho+B1:wght@600;800&display=swap">
<style>
  :root {
    --paper: #ffffff;
    --ink: #0d0d0d;
    --band-dark: #050505;
    --band-mid: #2a2a2a;
    --red: #c4161c;
    --red-deep: #8e0d12;
    --cream: #f3ead8;
    --white: #ffffff;
    --window-light: #f7ece6;
    --window-mid: #eccbbd;
    --window-warm: #e3a08c;
  }
  * { margin: 0; padding: 0; box-sizing: border-box; }
  html, body {
    width: 853px; height: 1200px; overflow: hidden;
    background: var(--paper);
    font-family: "Shippori Mincho B1", serif;
  }
  .canvas { position: relative; width: 853px; height: 1200px; }

  .variant-tag { position: absolute; top: 0; right: 0; width: 120px; height: 70px; }
  .variant-tag span {
    position: absolute; top: 10px; right: 14px;
    color: var(--white); font-size: 26px; font-weight: 600;
  }

  .bag {
    position: absolute; left: 94px; top: 105px; width: 668px; height: 965px;
    overflow: hidden;
  }
  .band-top {
    position: absolute; left: 0; top: 0; width: 100%; height: 107px;
    background: linear-gradient(180deg, var(--band-dark) 0%, var(--band-mid) 55%, var(--band-dark) 100%);
  }
  .contents-view {
    position: absolute; left: 0; top: 107px; width: 100%; height: 722px;
    background:
      radial-gradient(ellipse at 50% 45%, var(--window-light) 0%, var(--window-mid) 65%, var(--window-warm) 100%);
  }
  .band-bottom {
    position: absolute; left: 0; bottom: 0; width: 100%; height: 136px;
    background: linear-gradient(180deg, var(--band-dark) 0%, var(--band-mid) 50%, var(--band-dark) 100%);
  }

  .banner {
    position: absolute; left: 155px; top: 0; width: 238px; height: 914px;
    background: linear-gradient(90deg, var(--red-deep) 0%, var(--red) 12%, var(--red) 88%, var(--red-deep) 100%);
  }
  .vertical { writing-mode: vertical-rl; text-orientation: upright; }

  .origin {
    position: absolute; left: 164px; top: 155px; width: 70px; height: 170px;
    background: var(--cream); border: 3px solid var(--ink);
    display: flex; justify-content: center; align-items: center;
  }
  .origin-text { font-size: 38px; font-weight: 800; color: var(--ink); line-height: 1; }

  .grade {
    position: absolute; left: 72px; top: 164px;
    font-size: 58px; font-weight: 800; color: var(--white); line-height: 1;
  }
  .emblem { position: absolute; left: 87px; top: 308px; }

  .product-name {
    position: absolute; left: 146px; top: 392px;
    font-size: 62px; font-weight: 800; color: var(--white); line-height: 1;
    letter-spacing: 6px;
  }
  .tagline {
    position: absolute; left: 34px; top: 450px; height: 190px;
    font-size: 14px; font-weight: 600; color: var(--white);
    line-height: 25px; letter-spacing: 2px;
  }
  .maker {
    position: absolute; left: 141px; top: 795px; width: 62px; height: 86px;
    background: var(--cream); border: 2px solid var(--ink);
    display: flex; justify-content: center; align-items: center;
  }
  .maker-name { font-size: 20px; font-weight: 800; color: var(--ink); line-height: 26px; }
</style>
</head>
<body>
<div class="canvas">
  <div class="variant-tag">
    <svg width="120" height="70" viewBox="0 0 120 70"><polygon points="0,0 120,0 120,70" fill="#c4161c"/></svg>
    <span>A1</span>
  </div>

  <div class="bag">
    <div class="band-top"></div>
    <div class="contents-view" role="img" aria-label="透明窓から見えるパック詰めのかに身と湯気の模様"></div>
    <div class="band-bottom"></div>

    <div class="banner">
      <div class="origin"><span class="vertical origin-text">香住港産</span></div>
      <div class="vertical grade">特選</div>
      <svg class="emblem" width="80" height="80" viewBox="0 0 80 80" aria-hidden="true">
        <circle cx="40" cy="40" r="35" fill="none" stroke="#ffffff" stroke-width="5"/>
      </svg>
      <div class="vertical product-name">かに身</div>
      <p class="vertical tagline">日本海の深層水で<br>育まれた、かに本来の<br>極上の身を<br>お楽しみください</p>
      <div class="maker"><span class="vertical maker-name">北岡<br>商店</span></div>
    </div>
  </div>
</div>
</body>
</html>
```